Power point template for corporate use

We need a simple power point template to use with our new logo design for corporate presentations to prospects

Target Market(s)

Corporate marketing departments - clients purchase our services and data

```html
<!DOCTYPE html>
<html lang="en">
<head>
<meta charset="utf-8">
<title>Norvale Digital Marketing – Presentation Template</title>
<link rel="stylesheet" href="https://fonts.googleapis.com/css2?family=Roboto:wght@300;400;500;700;900&family=Roboto+Condensed:wght@300;400;700&display=swap">
<style>
:root{
  --red:#c9202f;
  --red-deep:#c21f2e;
  --ink:#2e2b2d;
  --band:#302d2f;
  --paper:#ffffff;
  --mist:#f3f3f3;
  --rule:#e4e4e4;
  --placeholder:#e8e8e8;
  --text:#4a4a4a;
  --mute:#777;
  --canvas:#b8b8ba;
  --blue:#0aa0d6;
  --green:#7cc242;
  --orange:#e8703a;
  --purple:#9a4cb8;
  --graph-dark:#3a3739;
  --graph-gray:#9a9a9a;
}
*{box-sizing:border-box;margin:0;padding:0}
html,body{width:1064px;height:1200px;overflow:hidden;background:var(--canvas)}
body{font-family:"Roboto",Arial,sans-serif;color:var(--text);position:relative}
.slide{position:absolute;width:516px;height:387px;background:var(--paper);overflow:hidden}
.s1{left:12px;top:9px;background:var(--mist)}
.s2{left:536px;top:9px}
.s3{left:12px;top:407px}
.s4{left:536px;top:407px}
.s5{left:12px;top:805px}
.s6{left:536px;top:805px;background:var(--red-deep)}
.abs{position:absolute}

/* slide headers */
.slide-head{position:absolute;left:0;top:0;width:100%;height:49px;border-bottom:1px solid var(--rule);text-align:center;background:#fafafa}
.slide-title{font-family:"Roboto Condensed",Arial,sans-serif;font-weight:300;color:var(--red);font-size:23px;line-height:1;padding-top:6px;letter-spacing:.2px}
.slide-sub{font-family:"Roboto Condensed",Arial,sans-serif;font-size:8px;color:var(--mute);margin-top:3px;text-transform:uppercase}
.slide-sub b{font-weight:700;color:#555}

/* footer band */
.slide-foot{position:absolute;left:0;bottom:0;width:100%;height:32px;background:var(--band);display:flex;align-items:center;padding-left:10px;font-size:8px;color:#fff}
.foot-name{font-weight:900;font-size:11px;color:#fff;margin-right:8px;letter-spacing:.3px}
.foot-red{color:var(--red);font-weight:500}
.foot-sep{margin:0 4px}
.foot-strong{font-weight:700}
.foot-page{position:absolute;right:10px;font-size:7px;color:var(--red)}

/* placeholder image */
.ph{position:absolute;background:var(--placeholder);border:1px solid #f0d0d4;display:flex;align-items:center;justify-content:center}
.ph svg{opacity:.9}

/* title slide */
.brand-big{position:absolute;left:0;width:100%;text-align:center;font-weight:900;letter-spacing:2px}
.s1 .brand-big{top:108px;font-size:62px;color:var(--ink)}
.brand-tag{position:absolute;left:0;width:100%;text-align:center;font-weight:500;letter-spacing:3.2px;font-size:15px}
.s1 .brand-tag{top:226px;color:var(--ink)}
.pres-title{position:absolute;right:14px;top:282px;text-align:right;font-family:"Roboto Condensed",Arial,sans-serif;font-size:18px;color:var(--ink)}
.pres-date{display:block;font-size:11px;color:var(--red);margin-top:2px}
.title-band{position:absolute;left:0;bottom:0;width:100%;height:64px;background:var(--band);padding:14px 0 0 10px}
.title-band .co{font-size:17px;color:#fff;font-family:"Roboto Condensed",Arial,sans-serif;font-weight:300}
.title-band .co b{font-weight:700}
.title-band .to{font-size:11px;color:var(--red);margin-top:1px}
.title-band .to b{font-weight:700}
.logo-slot{position:absolute;right:14px;bottom:9px;width:59px;height:45px;background:#454244;display:flex;align-items:center;justify-content:center}

/* landscape notes */
.note{position:absolute;left:36px;width:460px;display:flex;gap:8px;font-size:7px;line-height:1.35;color:var(--text)}
.note b{font-weight:700}
.note svg{flex:none}

/* portrait */
.content-title{position:absolute;left:64px;top:76px;font-size:14px;color:var(--text)}
.content-title b{font-weight:700}
.num{position:absolute;left:26px;width:32px;height:32px;border-radius:50%;background:var(--red);color:#fff;font-size:19px;display:flex;align-items:center;justify-content:center}
.para{position:absolute;left:64px;width:200px;font-size:8px;line-height:1.45;text-align:justify;color:var(--text)}
.para b{font-weight:700}
.list{position:absolute;left:82px;list-style:none;font-size:8px;color:var(--text)}
.list li{height:23.5px;display:flex;align-items:flex-start;gap:6px}

/* tables */
.tbl-title{position:absolute;top:70px;font-size:14px;display:flex;align-items:center;gap:6px;color:var(--text)}
.tbl-title b{font-weight:700}
table.grid{position:absolute;top:91px;width:230px;border-collapse:collapse;font-size:5.6px;table-layout:fixed}
table.grid th{height:21px;font-size:7.5px;font-weight:500;text-align:center}
table.grid td{height:22.4px;padding:0 3px;vertical-align:middle;line-height:1.2}
table.grid td:first-child{text-align:center;color:var(--red);font-size:8px}
table.grid td:nth-child(3),table.grid td:nth-child(4){text-align:center}
.light th{background:#3f3c3e;color:#ddd}
.light td{border-bottom:1px solid #e6e6e6;color:#555;background:#fff}
.dark th{background:var(--red);color:#fff}
.dark td{border-bottom:1px solid #555;color:#ccc;background:var(--band)}
.tbl-foot{position:absolute;top:314px;width:230px;height:23px;font-size:8.5px;font-weight:500;color:#fff;display:flex;align-items:center;justify-content:center}
.light-foot{background:var(--red)}
.dark-foot{background:var(--band)}

/* graphs */
.graph-title{position:absolute;top:76px;font-size:14px;color:var(--text)}
.graph-title b{font-weight:700}
.bullets{position:absolute;list-style:none;width:205px;font-size:6.6px;line-height:1.3;color:var(--text)}
.bullets li{position:relative;padding-left:12px;margin-bottom:8px}
.bullets li::before{content:"";position:absolute;left:0;top:2px;border-left:4px solid var(--red);border-top:2.5px solid transparent;border-bottom:2.5px solid transparent}
.bullets b{font-weight:700}

/* closing */
.s6 .brand-big{top:130px;font-size:62px;color:#fff}
.s6 .brand-tag{top:251px;color:#fff}
.contact{position:absolute;left:14px;font-size:7px;color:#fff;line-height:1.25}
.contact b{font-size:8.5px;font-weight:700;display:block}
.site{position:absolute;right:60px;bottom:12px;font-size:8px;color:#e0606b}
.socials{position:absolute;right:10px;bottom:11px;display:flex;gap:5px}
.socials span{width:10px;height:10px;border-radius:50%;background:#e0606b;display:block}
</style>
</head>
<body>

<!-- Title slide -->
<section class="slide s1">
  <div class="brand-big">NORVALE</div>
  <div class="brand-tag">DIGITAL MARKETING</div>
  <div class="pres-title">PRESENTATION TITLE<span class="pres-date">JAN 2014</span></div>
  <div class="title-band">
    <div class="co"><b>COMPANY</b> PRESENTATION</div>
    <div class="to">to <b>Business</b>/Client</div>
  </div>
  <div class="logo-slot">
    <svg width="22" height="18" viewBox="0 0 22 18"><rect x="1" y="1" width="20" height="16" fill="none" stroke="#c9202f" stroke-width="1.5"/><path d="M3 15 L9 8 L13 12 L16 9 L19 15Z" fill="#c9202f"/></svg>
  </div>
</section>

<!-- Landscape image slide -->
<section class="slide s2">
  <header class="slide-head">
    <h1 class="slide-title">IMAGE IN LANDSCAPE VIEW</h1>
    <p class="slide-sub">with completely <b>customizable</b> icons</p>
  </header>
  <div class="ph" style="left:34px;top:70px;width:448px;height:199px" role="img" aria-label="Landscape photograph placeholder">
    <svg width="94" height="94" viewBox="0 0 94 94"><rect x="3" y="3" width="88" height="88" fill="none" stroke="#d6d6d6" stroke-width="5"/><circle cx="30" cy="32" r="9" fill="#d6d6d6"/><path d="M12 78 L38 44 L52 62 L64 48 L82 78Z" fill="#d6d6d6"/></svg>
  </div>
  <div class="note" style="top:287px">
    <svg width="16" height="14" viewBox="0 0 16 14"><rect x="1" y="1" width="14" height="9" fill="none" stroke="#c9202f" stroke-width="1.6"/><path d="M5 13h6M8 10v3" stroke="#c9202f" stroke-width="1.6"/></svg>
    <p><b>Aenean</b> ridiculus tortor quis interdum id habitant ad, natoque consectetuer nisl auctor libero quisque euismod ante inceptos malesuada ligula mattis.</p>
  </div>
  <div class="note" style="top:318px">
    <svg width="16" height="14" viewBox="0 0 16 14"><path d="M1 5h4l8-4v12l-8-4H1Z" fill="none" stroke="#c9202f" stroke-width="1.6"/><path d="M4 9l1 4" stroke="#c9202f" stroke-width="1.6"/></svg>
    <p><b>Aenean</b> ridiculus tortor quis interdum id habitant ad, natoque consectetuer nisl auctor libero quisque euismod ante inceptos malesuada ligula mattis.</p>
  </div>
  <footer class="slide-foot"><span class="foot-name">NORVALE</span><span class="foot-red">DIGITAL MARKETING</span><span class="foot-sep">|</span><span class="foot-strong">COMPANY</span>&nbsp;PRESENTATION&nbsp;<span class="foot-red">to Business/client</span><span class="foot-page">3</span></footer>
</section>

<!-- Portrait image slide -->
<section class="slide s3">
  <header class="slide-head">
    <h1 class="slide-title">IMAGE IN PORTRAIT VIEW</h1>
    <p class="slide-sub">with an example of different typography</p>
  </header>
  <h2 class="content-title"><b>Content</b> title</h2>
  <div class="num" style="top:105px">1</div>
  <p class="para" style="top:98px"><b>Aenean</b> ridiculus tortor quis interdum id habitant ad, natoque consectetuer nisl auctor libero quisque euismod ante inceptos malesuada ligula mattis.</p>
  <ul class="list" style="top:156px">
    <li><svg width="8" height="8" viewBox="0 0 8 8"><path d="M1 4l2 3 4-7" fill="none" stroke="#c9202f" stroke-width="1.5"/></svg>Pellentesque</li>
    <li><svg width="8" height="8" viewBox="0 0 8 8"><path d="M1 4l2 3 4-7" fill="none" stroke="#c9202f" stroke-width="1.5"/></svg>Parturient</li>
    <li><svg width="8" height="8" viewBox="0 0 8 8"><path d="M1 4l2 3 4-7" fill="none" stroke="#c9202f" stroke-width="1.5"/></svg>Ridiculus</li>
  </ul>
  <div class="num" style="top:236px">2</div>
  <p class="para" style="top:228px"><b>Aenean</b> ridiculus tortor quis interdum id habitant ad, natoque consectetuer nisl auctor libero quisque euismod ante inceptos malesuada ligula mattis.</p>
  <ul class="list" style="top:285px">
    <li><svg width="9" height="8" viewBox="0 0 9 8"><path d="M0 4h6M4 1l4 3-4 3" fill="none" stroke="#c9202f" stroke-width="1.8"/></svg>Malesuada</li>
    <li><svg width="9" height="8" viewBox="0 0 9 8"><path d="M0 4h6M4 1l4 3-4 3" fill="none" stroke="#c9202f" stroke-width="1.8"/></svg>Consectetuer</li>
    <li><svg width="9" height="8" viewBox="0 0 9 8"><path d="M0 4h6M4 1l4 3-4 3" fill="none" stroke="#c9202f" stroke-width="1.8"/></svg>Natoque</li>
  </ul>
  <div class="ph" style="left:267px;top:64px;width:218px;height:275px;border-color:#ddd" role="img" aria-label="Portrait photograph placeholder">
    <svg width="94" height="94" viewBox="0 0 94 94"><rect x="3" y="3" width="88" height="88" fill="none" stroke="#d6d6d6" stroke-width="5"/><circle cx="30" cy="32" r="9" fill="#d6d6d6"/><path d="M12 78 L38 44 L52 62 L64 48 L82 78Z" fill="#d6d6d6"/></svg>
  </div>
  <footer class="slide-foot"><span class="foot-name">NORVALE</span><span class="foot-red">DIGITAL MARKETING</span><span class="foot-sep">|</span><span class="foot-strong">COMPANY</span>&nbsp;PRESENTATION&nbsp;<span class="foot-red">to Business/client</span><span class="foot-page">4</span></footer>
</section>

<!-- Tables slide -->
<section class="slide s4">
  <header class="slide-head">
    <h1 class="slide-title">COLOR STYLE TABLES</h1>
    <p class="slide-sub">choose from a <b>light</b> or <b>dark</b> theme</p>
  </header>
  <h2 class="tbl-title" style="left:20px"><svg width="16" height="13" viewBox="0 0 16 13"><rect x="1" y="1" width="14" height="11" fill="none" stroke="#c9202f" stroke-width="1.4"/><path d="M1 4.5h14M1 8h14M6 1v11M10.5 1v11" stroke="#c9202f" stroke-width="1.2"/></svg><span><b>Light</b> Theme</span></h2>
  <table class="grid light" style="left:20px">
    <colgroup><col style="width:30px"><col style="width:90px"><col style="width:62px"><col style="width:48px"></colgroup>
    <thead><tr><th>Item</th><th>Step/Action</th><th>Responsible</th><th>Target Date</th></tr></thead>
    <tbody>
      <tr><td>1</td><td>Business X, Y, Z high level needs</td><td>Business X, Y, Z</td><td>5/24/2013</td></tr>
      <tr><td>2</td><td>Understand current situation and safety mana</td><td>Business X, Y, Z</td><td>5/31/2013</td></tr>
      <tr><td>3</td><td>Submit Proposal</td><td>Business X, Y, Z</td><td>6/3/2013</td></tr>
      <tr><td>4</td><td>Review Proposal</td><td>Business X, Y, Z</td><td>TBD</td></tr>
      <tr><td>5</td><td>Prepare Final Proposal &amp; Statement of Work (SOW)</td><td>Business X, Y, Z</td><td>TBD</td></tr>
      <tr><td>6</td><td>Complete and sign SOW</td><td>Business X, Y, Z</td><td>TBD</td></tr>
      <tr><td>7</td><td>Schedule project start date</td><td>Business X, Y, Z</td><td>TBD</td></tr>
      <tr><td>8</td><td>Kick-off Project</td><td>Business X, Y, Z</td><td>TBD</td></tr>
      <tr><td>9</td><td>Complete Project</td><td>Business X, Y, Z</td><td>TBD</td></tr>
    </tbody>
  </table>
  <div class="tbl-foot light-foot" style="left:20px">• Additional Information</div>

  <h2 class="tbl-title" style="left:267px"><svg width="16" height="13" viewBox="0 0 16 13"><rect x="1" y="1" width="14" height="11" fill="none" stroke="#c9202f" stroke-width="1.4"/><path d="M1 4.5h14M1 8h14M6 1v11M10.5 1v11" stroke="#c9202f" stroke-width="1.2"/></svg><span><b>Dark</b> Theme</span></h2>
  <table class="grid dark" style="left:267px">
    <colgroup><col style="width:30px"><col style="width:90px"><col style="width:62px"><col style="width:48px"></colgroup>
    <thead><tr><th>Item</th><th>Step/Action</th><th>Responsible</th><th>Target Date</th></tr></thead>
    <tbody>
      <tr><td>1</td><td>Business X, Y, Z high level needs</td><td>Business X, Y, Z</td><td>5/24/2013</td></tr>
      <tr><td>2</td><td>Understand current situation and safety mana</td><td>Business X, Y, Z</td><td>5/31/2013</td></tr>
      <tr><td>3</td><td>Submit Proposal</td><td>Business X, Y, Z</td><td>6/3/2013</td></tr>
      <tr><td>4</td><td>Review Proposal</td><td>Business X, Y, Z</td><td>TBD</td></tr>
      <tr><td>5</td><td>Prepare Final Proposal &amp; Statement of Work (SOW)</td><td>Business X, Y, Z</td><td>TBD</td></tr>
      <tr><td>6</td><td>Complete and sign SOW</td><td>Business X, Y, Z</td><td>TBD</td></tr>
      <tr><td>7</td><td>Schedule project start date</td><td>Business X, Y, Z</td><td>TBD</td></tr>
      <tr><td>8</td><td>Kick-off Project</td><td>Business X, Y, Z</td><td>TBD</td></tr>
      <tr><td>9</td><td>Complete Project</td><td>Business X, Y, Z</td><td>TBD</td></tr>
    </tbody>
  </table>
  <div class="tbl-foot dark-foot" style="left:267px">• Additional Information</div>
  <footer class="slide-foot"><span class="foot-name">NORVALE</span><span class="foot-red">DIGITAL MARKETING</span><span class="foot-sep">|</span><span class="foot-strong">COMPANY</span>&nbsp;PRESENTATION&nbsp;<span class="foot-red">to Business/client</span><span class="foot-page">5</span></footer>
</section>

<!-- Graphs slide -->
<section class="slide s5">
  <header class="slide-head">
    <h1 class="slide-title">COLOR STYLE GRAPHS</h1>
    <p class="slide-sub">choose to use between <b>main</b> and <b>secondary</b> color themes</p>
  </header>
  <h2 class="graph-title" style="left:25px"><b>Graph</b> Main Colors</h2>
  <h2 class="graph-title" style="left:293px"><b>Graph</b> Secondary Colors</h2>

  <svg class="abs" style="left:0;top:0" width="516" height="387" viewBox="0 0 516 387">
    <g font-family="Roboto, Arial, sans-serif" font-size="7" fill="#333">
      <line x1="43" y1="105" x2="233" y2="105" stroke="#ddd" stroke-width=".6"/>
      <line x1="43" y1="142" x2="233" y2="142" stroke="#ddd" stroke-width=".6"/>
      <line x1="43" y1="180" x2="233" y2="180" stroke="#ddd" stroke-width=".6"/>
      <line x1="43" y1="217" x2="233" y2="217" stroke="#ddd" stroke-width=".6"/>
      <text x="26" y="107">100</text><text x="29" y="145">75</text><text x="29" y="182">50</text><text x="29" y="219">25</text><text x="32" y="253">0</text>
      <polygon points="43,176 106,191 169,150 233,156 233,254 43,254" fill="var(--graph-dark)"/>
      <polygon points="43,212 75,225 43,230" fill="var(--graph-gray)"/>
      <polygon points="43,229 106,217 169,175 233,117 233,254 43,254" fill="var(--red)"/>
      <line x1="43" y1="254" x2="233" y2="254" stroke="#555" stroke-width=".6"/>
      <text x="36" y="263">2007</text><text x="99" y="263">2008</text><text x="162" y="263">2009</text><text x="226" y="263">2010</text>
    </g>
    <g transform="translate(372,179)" font-family="Roboto, Arial, sans-serif" font-size="9" fill="#fff">
      <path d="M0 0 L77.4 32.6 A84 84 0 0 1 -46.5 70 Z" fill="var(--purple)"/>
      <path d="M0 0 L-46.5 70 A84 84 0 1 1 42 -72.7 Z" fill="var(--blue)"/>
      <path d="M0 0 L74.5 -38.9 A84 84 0 0 1 77.4 32.6 Z" fill="var(--orange)"/>
      <path d="M6 -6 L48 -78.7 A84 84 0 0 1 80.5 -44.9 Z" fill="var(--green)" stroke="#fff" stroke-width="1.5"/>
      <text x="-44" y="-17">50%</text>
      <text x="48" y="-14">9%</text>
      <text x="48" y="18">14%</text>
      <text x="8" y="53">28%</text>
    </g>
    <g font-family="Roboto, Arial, sans-serif" font-size="6.5" fill="#333">
      <circle cx="462" cy="228" r="3" fill="var(--green)"/><text x="468" y="230.5">2007</text>
      <circle cx="462" cy="237" r="3" fill="var(--orange)"/><text x="468" y="239.5">2008</text>
      <circle cx="462" cy="246" r="3" fill="var(--purple)"/><text x="468" y="248.5">2009</text>
      <circle cx="462" cy="255" r="3" fill="var(--blue)"/><text x="468" y="257.5">2010</text>
    </g>
  </svg>

  <ul class="bullets" style="left:36px;top:275px">
    <li><b>Aenean</b> ridiculus tortor quis interdum id habitant ad, natoque consectetuer nisl auctor libero quisque euismod ante inceptos malesuada ligula mattis.</li>
    <li>Varius inceptos <b>nascetur</b> mollis dui aptent ultrices. Pretium pulvinar ante lobortis convallis lectus netus vitae penatibus eros at blandit. Parturient.</li>
  </ul>
  <ul class="bullets" style="left:289px;top:275px">
    <li><b>Aenean</b> ridiculus tortor quis interdum id habitant ad, natoque consectetuer nisl auctor libero quisque euismod ante inceptos malesuada ligula mattis.</li>
    <li>Varius inceptos <b>nascetur</b> mollis dui aptent ultrices. Pretium pulvinar ante lobortis convallis lectus netus vitae penatibus eros at blandit. Parturient.</li>
  </ul>
  <footer class="slide-foot"><span class="foot-name">NORVALE</span><span class="foot-red">DIGITAL MARKETING</span><span class="foot-sep">|</span><span class="foot-strong">COMPANY</span>&nbsp;PRESENTATION&nbsp;<span class="foot-red">to Business/client</span><span class="foot-page">7</span></footer>
</section>

<!-- Closing slide -->
<section class="slide s6">
  <div class="brand-big">NORVALE</div>
  <div class="brand-tag">DIGITAL MARKETING</div>
  <div class="contact" style="top:311px"><b>Contact us:</b>555-010-0188<br>info@norvaledigital.com</div>
  <div class="contact" style="top:351px"><b>Central Office:</b>Address Line 1<br>Address Line 2</div>
  <div class="site">www.norvaledigital.com</div>
  <div class="socials"><span></span><span></span><span></span></div>
</section>

</body>
</html>
```